Tidal Fern Business Cards

We need something new, fun and exciting for business cards. Our current ones are just plain and we need a design that pops. We want name, position held, phone, email on the front, and a 20% discount on the back. I have also uploaded our old business cards creative to see what we are not wanting, and how boring they were and we want something jazzed up from this, cool design and catches people attention.

```html
<!DOCTYPE html>
<html lang="en">
<head>
<meta charset="utf-8">
<title>Tidal Fern Business Cards</title>
<link rel="stylesheet" href="https://fonts.googleapis.com/css2?family=Lexend:wght@300;400;600&family=Montserrat:wght@400;700&display=swap">
<style>
  :root {
    --backdrop: #e8e3da;
    --paper: #ffffff;
    --navy: #1b3d74;
    --navy-deep: #183868;
    --coral: #f0706a;
    --ink: #1e3a6e;
    --white: #ffffff;
  }
  * { margin: 0; padding: 0; box-sizing: border-box; }
  html, body { width: 1200px; height: 859px; overflow: hidden; }
  body { background: var(--backdrop); position: relative; font-family: "Lexend", sans-serif; }

  .card {
    position: absolute;
    top: 289px;
    width: 500px;
    height: 285px;
    border-radius: 2px;
    box-shadow: 0 6px 14px rgba(0,0,0,0.18);
  }
  .card--front { left: 60px; background: var(--paper); }
  .card--back { left: 639px; background: var(--navy); }

  .brand {
    position: absolute;
    left: 76px;
    top: 52px;
    display: flex;
    align-items: center;
    gap: 18px;
  }
  .brand__dot {
    width: 40px; height: 40px;
    border-radius: 50%;
    background: var(--coral);
  }
  .brand__name {
    font-family: "Lexend", sans-serif;
    font-weight: 600;
    font-size: 48px;
    color: var(--ink);
    letter-spacing: -0.5px;
    line-height: 1;
  }

  .rule {
    position: absolute;
    left: 22px; right: 22px;
    top: 154px;
    height: 1px;
    background: var(--coral);
  }

  .person {
    position: absolute;
    left: 71px;
    top: 201px;
  }
  .person__name {
    font-family: "Montserrat", sans-serif;
    font-weight: 700;
    font-size: 14px;
    letter-spacing: 0.6px;
    color: var(--coral);
    text-transform: uppercase;
    line-height: 1.2;
  }
  .person__role {
    font-weight: 400;
    font-size: 13px;
    color: var(--ink);
    line-height: 1.3;
  }

  .divider {
    position: absolute;
    left: 258px;
    top: 201px;
    width: 1px;
    height: 30px;
    background: var(--ink);
  }

  .contact {
    position: absolute;
    left: 276px;
    top: 201px;
    list-style: none;
    font-weight: 300;
    font-size: 13px;
    color: var(--ink);
    line-height: 17px;
  }
  .contact li { display: flex; align-items: center; gap: 6px; }
  .contact svg { width: 11px; height: 11px; flex: none; }

  .seal {
    position: absolute;
    left: 150px;
    top: 35px;
    width: 200px;
    height: 200px;
  }
  .seal__text {
    font-family: "Montserrat", sans-serif;
    font-weight: 700;
    font-size: 15px;
    fill: var(--white);
  }

  .offer {
    position: absolute;
    left: 0; right: 0;
    top: 254px;
    text-align: center;
    font-family: "Montserrat", sans-serif;
    font-size: 15px;
    color: var(--white);
    letter-spacing: 0.3px;
  }
  .offer__amount { color: var(--coral); font-weight: 700; }
</style>
</head>
<body>
  <section class="card card--front" aria-label="Business card front">
    <div class="brand">
      <span class="brand__dot"></span>
      <span class="brand__name">Tidal Fern</span>
    </div>
    <div class="rule"></div>
    <div class="person">
      <p class="person__name">Marlo Penning</p>
      <p class="person__role">Sales Manager</p>
    </div>
    <div class="divider"></div>
    <ul class="contact">
      <li>
        <svg viewBox="0 0 12 12" aria-hidden="true"><circle cx="6" cy="6" r="5" fill="none" stroke="#f0706a" stroke-width="1"/><path d="M4 3.5c0 2.5 1.8 4.6 4.5 4.8l.5-1.2-1.3-.6-.6.6c-.9-.4-1.6-1.1-2-2l.6-.6-.6-1.3z" fill="#f0706a"/></svg>
        (555) 014-2780
      </li>
      <li>
        <svg viewBox="0 0 12 12" aria-hidden="true"><rect x="0.8" y="2.5" width="10.4" height="7" fill="none" stroke="#f0706a" stroke-width="1"/><path d="M0.8 2.5 6 6.6l5.2-4.1" fill="none" stroke="#f0706a" stroke-width="1"/></svg>
        info@tidalfern.com
      </li>
    </ul>
  </section>

  <section class="card card--back" aria-label="Business card back">
    <svg class="seal" viewBox="0 0 200 200" aria-label="Be Tidal, Fern Tidal Fern">
      <defs>
        <path id="seal-ring" d="M100,100 m-82,0 a82,82 0 1,1 164,0 a82,82 0 1,1 -164,0"/>
      </defs>
      <text class="seal__text" dy="5">
        <textPath href="#seal-ring" startOffset="2%" textLength="470" lengthAdjust="spacing">BE TIDAL, FERN  TIDAL FERN</textPath>
      </text>
      <circle cx="100" cy="100" r="22" fill="#f0706a"/>
    </svg>
    <p class="offer"><span class="offer__amount">20%</span> DISCOUNT</p>
  </section>
</body>
</html>
```